International Food Manufacturer in the need of a new business card and logo.

Our Company - Northgate Pantry Ltd.

Our Industry - Food and Drink

We are a Wild Harvested Food Distributor / Manufacturer. We service the following food sectors: Supermarkets, Hotels, Restaurants, Cafes, Catering and all people looking to eat healthy food products.

Slogan - The foremost source for everything healthy

Business card details -

48-52 Marlow Lane
Hatherby Green
London
EC9Z 4RT United Kingdom
Dennis Prowle
+44 7000 481736 - UK
+971 50 7739205 - UAE
+38 063 914 2758 - Ukraine
dennis@northgatepantry.example
www.northgatepantry.example

Goal - We are looking for a dynamic modern new look for our corporate image and a designer who can bring this new concept to our future food product designs. Please try to incorporate 3d hexagonal vector Imaging in your design concepts.

Target Market(s)

Industry/Entity Type

Food Service

Contact Information for Business Card

Northgate Pantry Ltd.
48-52 Marlow Lane
Hatherby Green
London
EC9Z 4RT United Kingdom
Dennis Prowle
+44 7000 481736 - UK
+971 50 7739205 - UAE

Font styles to use
Serif

Colors

Designer to choose colors to be used in the design.

Requirements
Must have
• Please read project description above.
Nice to have
Should not have

```html
<!DOCTYPE html>
<html lang="en">
<head>
<meta charset="utf-8">
<title>Northgate Pantry Ltd. – Business Card</title>
<link rel="stylesheet" href="https://fonts.googleapis.com/css2?family=Libre+Baskerville&family=Roboto:wght@400;500&family=Roboto+Condensed:wght@400;700&display=swap">
<style>
  :root {
    --bg: #e9e7e3;
    --card: #ffffff;
    --card-shade: #f1f1f1;
    --ink: #1a1a1a;
    --ink-soft: #555555;
    --rule: #8a8a8a;
    --band: #141414;
    --band-text: #f5f5f5;
  }
  * { margin: 0; padding: 0; box-sizing: border-box; }
  html, body { width: 1200px; height: 1023px; overflow: hidden; background: var(--bg); }
  .stage { position: relative; width: 1200px; height: 1023px; }
  .card {
    position: absolute; left: 100px; top: 226px; width: 1000px; height: 571px;
    background: linear-gradient(160deg, var(--card) 40%, var(--card-shade));
    border-radius: 22px; overflow: hidden;
    box-shadow: 0 12px 40px rgba(0,0,0,.18);
    font-family: "Roboto", sans-serif; color: var(--ink);
  }
  .company {
    position: absolute; left: 52px; top: 44px;
    font-family: "Libre Baskerville", serif; font-size: 52px; letter-spacing: 1px;
    color: var(--ink); white-space: nowrap;
  }
  .company-rule { position: absolute; left: 52px; top: 120px; width: 880px; height: 1.5px; background: var(--rule); }
  .tagline-row { position: absolute; left: 52px; top: 140px; display: flex; align-items: center; gap: 14px; }
  .tagline-row .rule { width: 90px; height: 1.5px; background: var(--rule); }
  .tagline { font-family: "Roboto Condensed", sans-serif; font-size: 20px; letter-spacing: 1.2px; color: var(--ink-soft); }

  .person { position: absolute; right: 0; top: 212px; text-align: right; }
  .person .name {
    display: flex; align-items: center; justify-content: flex-end; gap: 14px;
    font-family: "Roboto Condensed", sans-serif; font-weight: 700; font-size: 38px; letter-spacing: .5px;
  }
  .person .name .block { width: 34px; height: 44px; background: var(--band); }
  .person-rule { position: absolute; right: 0; top: 262px; width: 560px; height: 1.5px; background: var(--ink); }
  .role { position: absolute; right: 60px; top: 268px; font-family: "Roboto Condensed", sans-serif; font-size: 17px; letter-spacing: 1.5px; color: var(--ink-soft); }

  .address { position: absolute; right: 60px; top: 306px; text-align: right; font-size: 20px; line-height: 1.45; color: var(--ink-soft); }

  .divider { position: absolute; left: 430px; top: 195px; width: 1.5px; height: 260px; background: var(--rule); transform: rotate(0deg); }

  .contacts { position: absolute; left: 52px; top: 300px; list-style: none; font-size: 20px; line-height: 1.5; color: var(--ink-soft); }
  .contacts li { display: flex; align-items: center; gap: 12px; }
  .contacts svg { width: 15px; height: 15px; flex: none; fill: none; stroke: var(--ink-soft); stroke-width: 1.6; }

  .service-band {
    position: absolute; left: 0; right: 0; bottom: 0; height: 62px; background: var(--band);
    display: flex; align-items: center; padding-left: 52px;
    font-family: "Roboto Condensed", sans-serif; font-size: 25px; letter-spacing: .8px; color: var(--band-text);
  }
</style>
</head>
<body>
<main class="stage">
  <article class="card">
    <h1 class="company">NORTHGATE PANTRY LTD.</h1>
    <div class="company-rule"></div>
    <div class="tagline-row"><span class="rule"></span><p class="tagline">THE FOREMOST SOURCE FOR EVERYTHING HEALTHY</p></div>

    <div class="person"><div class="name">ALDEN CREWE <span class="block"></span></div></div>
    <div class="person-rule"></div>
    <p class="role">DIRECTOR</p>

    <address class="address" style="font-style:normal">
      48-52 Marlow Lane<br>
      Hatherby Green London<br>
      EC9Z 4RT United Kingdom<br>
      Dennis Prowle
    </address>

    <div class="divider"></div>

    <ul class="contacts">
      <li><svg viewBox="0 0 16 16"><path d="M4 2l2.5 3-1.5 1.5c1 2 2.5 3.5 4.5 4.5L11 9.5l3 2.5-1.5 2C7.5 14 2 8.5 2 3.5z"/></svg>+44 7000 481736 - UK</li>
      <li><svg viewBox="0 0 16 16"><rect x="4" y="1.5" width="8" height="13" rx="1.5"/><path d="M7 12.5h2"/></svg>+971 50 7739205 - UAE</li>
      <li><svg viewBox="0 0 16 16"><circle cx="8" cy="8" r="6"/><path d="M8 2v12M2 8h12"/></svg>+38 063 914 2758 - Ukraine</li>
      <li><svg viewBox="0 0 16 16"><rect x="1.5" y="3.5" width="13" height="9" rx="1"/><path d="M1.5 4l6.5 5 6.5-5"/></svg>dennis@northgatepantry.example</li>
      <li><svg viewBox="0 0 16 16"><circle cx="8" cy="8" r="6.5"/><path d="M1.5 8h13M8 1.5c-3 3.5-3 9.5 0 13M8 1.5c3 3.5 3 9.5 0 13"/></svg>www.northgatepantry.example</li>
    </ul>

    <div class="service-band">OUR SERVICE : SUPERMARKETS, HOTELS, RESTAURANTS, CAFES,</div>
  </article>
</main>
</body>
</html>
```